Business Card Design Project

Business Card
We are rebranding with a new logo
Industry/Entity Type
Business
Contact Information for Business Card
Dennis Marlow +61 427581962 dennis@qovo.com.au P.O. Box 872 Kelvindale QLD 4309
Requirements
Must have
- Logo

```html
<!DOCTYPE html>
<html lang="en">
<head>
<meta charset="utf-8">
<title>Qovo International – Business Card</title>
<link rel="stylesheet" href="https://fonts.googleapis.com/css2?family=Rubik:wght@500;700&family=Questrial&display=swap">
<style>
  :root {
    --backdrop: #e9e6e1;
    --card-white: #f7f7f7;
    --brand-blue: #19ace3;
    --brand-orange: #ef7d2c;
    --panel-dark: #262626;
    --text-light: #ffffff;
    --icon-ink: #262626;
  }
  * { margin: 0; padding: 0; box-sizing: border-box; }
  html, body {
    width: 1200px; height: 800px; overflow: hidden;
    background: var(--backdrop);
  }
  .canvas { position: relative; width: 1200px; height: 800px; }

  .card {
    position: absolute; top: 235px;
    width: 520px; height: 330px;
    background: var(--card-white);
    overflow: hidden;
    box-shadow: 0 6px 18px rgba(0,0,0,0.18);
  }
  .card--front { left: 60px; }
  .card--back { left: 620px; }

  .brand-name {
    font-family: "Rubik", sans-serif;
    font-weight: 500;
    color: var(--brand-orange);
    white-space: nowrap;
    letter-spacing: 1px;
  }
  .card--front .brand-name {
    position: absolute; left: 0; right: 0; top: 130px;
    text-align: center; font-size: 34px;
  }
  .front-band { position: absolute; left: 0; bottom: 0; width: 520px; height: 50px; }

  .card--back .brand-name {
    position: absolute; left: 20px; top: 95px;
    font-size: 20px;
  }
  .back-panel { position: absolute; left: 0; top: 0; width: 520px; height: 330px; }

  .holder-name {
    position: absolute; left: 300px; top: 48px;
    font-family: "Rubik", sans-serif; font-weight: 700;
    font-size: 22px; color: var(--text-light);
  }
  .contact-line {
    position: absolute; left: 286px;
    font-family: "Questrial", sans-serif;
    font-size: 14.5px; line-height: 19px; color: var(--text-light);
  }
  .contact-line--phone { top: 155px; }
  .contact-line--email { top: 211px; }
  .contact-line--address { top: 256px; }

  .contact-icon { position: absolute; left: 236px; width: 28px; height: 28px; }
</style>
</head>
<body>
<main class="canvas">

  <section class="card card--front" aria-label="Card front">
    <div class="brand-name">Qovo International</div>
    <svg class="front-band" viewBox="0 0 520 50" aria-hidden="true">
      <path d="M0 18 H248 Q256 18 260 6 Q264 18 272 18 H520 V50 H0 Z" fill="var(--brand-blue)"/>
    </svg>
  </section>

  <section class="card card--back" aria-label="Card back">
    <svg class="back-panel" viewBox="0 0 520 330" aria-hidden="true">
      <rect x="262" y="0" width="258" height="330" fill="var(--panel-dark)"/>
      <rect x="231" y="0" width="31" height="330" fill="var(--brand-blue)"/>
      <g fill="var(--brand-blue)">
        <path d="M261 47 L279 63 L261 79 Z"/>
        <path d="M261 149 L279 165 L261 181 Z"/>
        <path d="M261 204 L279 220 L261 236 Z"/>
        <path d="M261 259 L279 275 L261 291 Z"/>
      </g>
      <g fill="#ffffff">
        <circle cx="250" cy="63" r="14"/>
        <circle cx="250" cy="165" r="14"/>
        <circle cx="250" cy="220" r="14"/>
        <circle cx="250" cy="275" r="14"/>
      </g>
      <!-- person -->
      <g fill="var(--icon-ink)">
        <circle cx="250" cy="59" r="3.4"/>
        <path d="M243.5 69 Q244 63.5 250 63.5 Q256 63.5 256.5 69 Z"/>
      </g>
      <!-- phone -->
      <path d="M245 159 L248 158.5 L249.5 162 L247.8 163.4 Q249.5 167 252.6 168.3 L254 166.6 L257.5 168 L257 171 Q249 172 245 159 Z" fill="var(--icon-ink)"/>
      <!-- globe -->
      <g fill="none" stroke="var(--icon-ink)" stroke-width="1.2">
        <circle cx="250" cy="220" r="6"/>
        <ellipse cx="250" cy="220" rx="2.6" ry="6"/>
        <line x1="244" y1="220" x2="256" y2="220"/>
        <line x1="245" y1="216.8" x2="255" y2="216.8"/>
        <line x1="245" y1="223.2" x2="255" y2="223.2"/>
      </g>
      <!-- pin -->
      <path d="M250 282 Q244.5 275 244.5 272 A5.5 5.5 0 0 1 255.5 272 Q255.5 275 250 282 Z M250 270 A2 2 0 1 0 250.01 270 Z" fill="var(--icon-ink)" fill-rule="evenodd"/>
    </svg>

    <div class="brand-name">Qovo International</div>

    <h1 class="holder-name">Dennis Marlow</h1>
    <p class="contact-line contact-line--phone">+61 427581962</p>
    <p class="contact-line contact-line--email">dennis@qovo.com.au</p>
    <p class="contact-line contact-line--address">P.O. Box 872<br>Kelvindale QLD 4309</p>
  </section>

</main>
</body>
</html>
```